Salon industry management software needs folded self-mailer flyer for direct mail

We are looking for a postcard / flyer folded self-mailer design for an 8.5" x 11" card stock printed both sides and folded in half to be the same end size as a 5.5" x 8.5" postcard. So, DOUBLE THE CONTENT from a regular postcard. See mailer attachment for the format we are looking for.
This will be to advertise our salon and spa management software to hair salons, spas, tanning salons, tattoo studios, and massage therapists. Our websites are https://parlorpilot-systems.net/ and https://brightloomsuite.net/ where you can get inspiration and some content. We have two software applications. Lumera is a desktop application and Vantel is a web application, so you can focus on one, both or a combination.
We need space for a QR code and of course mailing information.

Target Market(s)

salon, spa, tanning, tattoo, massage

Requirements
Must have
• content for four 5.5" x 8.5" pages including mailing info
Nice to have
• call to action, qr code

```html
<!DOCTYPE html>
<html lang="en">
<head>
<meta charset="utf-8">
<title>Lumera &amp; Vantel Self-Mailer</title>
<link rel="stylesheet" href="https://fonts.googleapis.com/css2?family=Roboto:wght@400;500;700&display=swap">
<style>
  :root {
    --bg: #e6e7e9;
    --green: #1f8a4c;
    --green-deep: #155f3c;
    --slate: #3a4f58;
    --pink: #e35a72;
    --teal: #1d7a8c;
    --ink: #222;
    --mist: #d8ece1;
  }
  * { box-sizing: border-box; margin: 0; padding: 0; }
  html, body { width: 1050px; height: 1200px; overflow: hidden; }
  body { background: var(--bg); font-family: "Roboto", Arial, sans-serif; color: var(--ink); position: relative; }
  .page { position: absolute; top: 275px; width: 500px; height: 650px; background: #fff; overflow: hidden; box-shadow: 0 4px 14px rgba(0,0,0,.18); }
  .page--mailer { left: 17px; }
  .page--features { left: 533px; }

  /* mailer side */
  .hero-photo { position: absolute; left: 0; top: 0; width: 500px; height: 322px;
    background: linear-gradient(100deg, #cfd0d3 0%, #e8e8ea 45%, #d9d3cf 70%, #f2f2f2 100%); }
  .address-line { position: absolute; left: 33px; width: 180px; height: 1px; background: #333; }
  .stamp-box { position: absolute; left: 33px; top: 197px; width: 53px; height: 63px; border: 1px solid #333; background: #fff;
    display: flex; align-items: center; justify-content: center; }
  .stamp-box span { transform: rotate(180deg); font-style: italic; font-size: 12px; font-family: Georgia, serif; }
  .green-panel { position: absolute; left: 0; top: 322px; width: 500px; height: 328px;
    background: linear-gradient(180deg, #1d6b47 0%, var(--green) 55%, #1b7a45 100%); }
  .salon-interior { position: absolute; inset: 0; background: linear-gradient(90deg, rgba(0,0,0,0) 0%, rgba(40,70,70,.35) 60%, rgba(30,60,70,.5) 100%); }
  .brand-row { position: absolute; top: 18px; right: 22px; display: flex; gap: 22px; align-items: center; }
  .brand { display: flex; align-items: center; gap: 6px; color: #fff; font-size: 22px; font-weight: 400; }
  .brand i { width: 10px; height: 10px; border-radius: 50%; background: #fff; display: block; }
  .headline { position: absolute; left: 0; top: 44px; }
  .headline .line1 { display: inline-block; background: var(--slate); color: #fff; font-weight: 700; font-size: 29px; line-height: 28px; padding: 0 8px 0 17px; }
  .headline .line2 { display: block; width: max-content; background: var(--pink); color: #fff; font-weight: 500; font-size: 23px; line-height: 25px; padding: 0 6px 0 17px; }
  .tagline { position: absolute; left: 17px; top: 108px; color: #fff; font-size: 15px; line-height: 18px; width: 230px; }
  .devices { position: absolute; left: 20px; top: 170px; width: 300px; height: 150px; border-radius: 4px;
    background: radial-gradient(ellipse at 50% 45%, rgba(240,240,242,.85) 0%, rgba(200,205,210,.55) 45%, rgba(30,30,30,.0) 80%); }

  /* features side */
  .wash { position: absolute; left: 0; top: 0; width: 500px; height: 360px;
    background: radial-gradient(ellipse at 45% 40%, var(--mist) 0%, rgba(216,236,225,.6) 45%, rgba(255,255,255,0) 75%); }
  .band { position: absolute; color: #fff; font-weight: 500; }
  .band--features { left: 33px; top: 29px; width: 437px; height: 25px; font-size: 16.5px; line-height: 25px; padding-left: 8px;
    background: linear-gradient(90deg, var(--green) 0%, var(--green) 70%, var(--slate) 100%); }
  .band--why { left: 8px; top: 360px; width: 340px; height: 25px; font-size: 16.5px; line-height: 25px; padding-left: 25px;
    background: linear-gradient(90deg, var(--green) 0%, var(--green) 60%, var(--slate) 100%); }
  .feature-list { position: absolute; left: 32px; top: 84px; list-style: none; }
  .feature-list li { margin-bottom: 12px; }
  .feature-list h3 { color: var(--teal); font-size: 11.5px; font-weight: 500; line-height: 14px; }
  .feature-list p { font-size: 9.5px; line-height: 12px; }
  .photo-circle { position: absolute; border-radius: 50%; }
  .photo-circle--owner { left: 283px; top: 111px; width: 194px; height: 194px; background: radial-gradient(circle at 55% 45%, #e8e2dc 0%, #3d7f8f 55%, #24606e 100%); }
  .photo-circle--team { left: 335px; top: 291px; width: 150px; height: 150px; background: radial-gradient(circle at 50% 50%, #e9dccd 0%, #b9b2aa 55%, #6b6761 100%); }
  .why-copy { position: absolute; left: 32px; top: 400px; width: 290px; font-size: 8.6px; line-height: 13px; }
  .sub-block { position: absolute; left: 32px; width: 455px; }
  .sub-block h4 { font-size: 11px; font-weight: 500; line-height: 13px; }
  .sub-block p { font-size: 8.2px; line-height: 11px; }
  .sub-block--dedicated { top: 480px; }
  .sub-block--dedicated h4 { color: var(--slate); }
  .sub-block--easy { top: 528px; }
  .sub-block--easy h4 { color: var(--teal); }
  .salon-strip { position: absolute; left: 0; top: 568px; width: 500px; height: 82px;
    background: linear-gradient(180deg, rgba(255,255,255,1) 0%, #b5a698 30%, #6e5c4e 70%, #4a3b33 100%); }
</style>
</head>
<body>

<section class="page page--mailer">
  <div class="hero-photo" role="img" aria-label="Soft faded photo of a smiling woman with long hair, printed upside down"></div>
  <div class="address-line" style="top:64px"></div>
  <div class="address-line" style="top:95px"></div>
  <div class="address-line" style="top:127px"></div>
  <div class="address-line" style="top:158px"></div>
  <div class="stamp-box"><span>Stamp</span></div>

  <div class="green-panel">
    <div class="salon-interior" role="img" aria-label="Green-tinted salon interior with styling chairs and mirrors"></div>
    <div class="brand-row">
      <div class="brand"><i></i>Lumera</div>
      <div class="brand"><i></i>Vantel</div>
    </div>
    <div class="headline">
      <span class="line1">SALON &amp; SPA</span>
      <span class="line2">Management Software</span>
    </div>
    <p class="tagline">Get the tools you need to grow your business!</p>
    <div class="devices" role="img" aria-label="Laptop, monitor, tablet and phone showing the scheduling software"></div>
  </div>
</section>

<section class="page page--features">
  <div class="wash"></div>
  <div class="band band--features">Vantel Spa and Salon Management Software Features</div>

  <ul class="feature-list">
    <li><h3>Appointment Scheduling</h3><p>Easily manage appointments and resources</p></li>
    <li><h3>Email Marketing</h3><p>Build your brand and keep clients engaged</p></li>
    <li><h3>Inventory Control</h3><p>Track your inventory and sell more products</p></li>
    <li><h3>Client Management</h3><p>Develop long-lasting relationships with your clients</p></li>
    <li><h3>Employee Management</h3><p>Save time and eliminate the stress</p></li>
    <li><h3>Point of Sale</h3><p>Complete transactions more efficiently and accurately</p></li>
  </ul>

  <div class="photo-circle photo-circle--owner" role="img" aria-label="Smiling salon owner holding a welcome we are open sign"></div>
  <div class="photo-circle photo-circle--team" role="img" aria-label="Two women looking at a tablet together"></div>

  <div class="band band--why">Why Lumera Spa &amp; Salon Software?</div>

  <p class="why-copy">For over 29 years, we have been helping salons, spas, barber shops, and other businesses to overcome their challenges and exceed their objectives. Our mission is to help you grow your business by developing an intuitive &amp; customizable software program and providing unparalleled customer service.</p>

  <div class="sub-block sub-block--dedicated">
    <h4>DEDICATED TO YOU</h4>
    <p>Salons &amp; spas consistently rave about our customer support. We don’t believe in “email support with 24-hour response times.” When you call us, you talk to a live person who is committed to helping you in whatever way we can.</p>
  </div>
  <div class="sub-block sub-block--easy">
    <h4>EASY TO USE</h4>
    <p>New technologies tend to be overwhelming. We’ve designed Lumera to be super simple to use. With our intuitive interface and familiar menus, you’ll be a pro in no time.</p>
  </div>

  <div class="salon-strip" role="img" aria-label="Stylists working on clients in a busy salon"></div>
</section>

</body>
</html>
```